The Bramblewood Roadside Defense Guide
An Owner's Notes on Quietly Settling Every Old Dispute
The Bramblewood Roadside Defense Guide - Law
This book will be read by middle class, well educated people with pending reckless driving charges.
Dimensions are approximately 6.5" x 8.5" (half sheet). We would like the title, sub title and the author's name ( Owen T. Marsh) to appear on the front cover. No text on the spine (about 1/8" spine). The back page will have no text. but the design on the back cover should allow us to place a text layer on top of the back cover design - so the back cover design should not make it difficult to read the text. (See attached example from previous project)
omarsh omarsh
#99 #100 #101 Submissions should not have any text on the back cover. Please remove the text from the back cover if you want your submission to be considered.
#61 - Can you do some variations of the text. Perhaps tweak the color or the color gradient.
#36 #66 #61 #45 #42 #53 #45 These are the top contenders. These are all awesome designs! To be selected the design must include back and front covers and NOT contain "2nd edition"
#36 #66 #61 #45 To be considered you must have a back cover as well as a front cover. Please resubmit your design with a back cover
#61 Can you take off the "2nd edition" from the front - this is not the second edition.
#14 my wife likes this one so that is a plus.:)
#7 this looks like a book on Velvet Harbor - Awesome! but probably not a great angle for a law firm :) I wonder if they would sue me if we just put a crystal pyramid and rainbow on the cover?
#11 nice design but too similar to the DUI book cover.
#14 Reckless driving cases are 80% speed related so the cover matches the subject well and it breaks away from the frame clip art pack nicely. The is something about it that says "Car ad" rather than legal book though. Maybe its the bright colors and contemporary "smart car" looking vehicle. May be look for different versions of the same theme and see.
#23 - forgot the title.
#20 I like the dirty scratched texture you did in #8 better, it makes it seem more interesting. #8's texturing is pretty heavy though, a slightly toned version, something in between #8 and #20 might be a good idea, no 100% sure though. I still think there needs to be some original graphic on the cover instead of just the text or framed clip art.
#9 I like that you are creating original images instead of just using the clip art whole-cloth and getting rid of the borders. That doesn't mean that a submission couldn't have a square frame clip art, it just means that originality scores points.
#22 Not bad, but the simplicity takes away from the professionalism. The look is not bad but then you realize its just swirled sirens with the clip art pasted on top. If the cover image was something original or it used some original elements in it I think it would help overcome that. I really like that your submissions are all over the place and not just a different versions of the same thing.
#19 I like that concept of this design. Its abstract, not just clip art photography pastes on the cover. Its completely unique from the other too examples of book covers. The colors and text are not my favorite. So the execution is not there yet but the fact that it is completely going off on its own is a big plus.
#8 I like the design of the scratched surface and the yellow hash marks...but it seems a little off. I don't know that the clip art I uploaded really matches. I can't help but wonder if something with traffic cones or a speed limit sign might be better. Don't know for sure...just vague impressions.
#21 this looks too similar to what we already have and is not very contemporary. Keep trying though.
#18 is a bit too similar to the DUI book cover I uploaded as an example. I don't want to be derivative.
#1 I think the police tap doesn't really match the Reckless driving. Most reckless driving cases are for speeding or minor car accidents, falling asleep at the wheel or someone doing doughnuts in a parking lot. Police crime scene tape doesn't usually come into play.
#2,#,3,#4 I marked these low because this is a reckless driving book not DUI. Reckless driving is not generally an alcohol offense in Va and so the covers' designs were a bit confusing.

```html
<!DOCTYPE html>
<html lang="en">
<head>
<meta charset="utf-8">
<title>The Bramblewood Roadside Defense Guide – Cover Spread</title>
<link rel="stylesheet" href="https://fonts.googleapis.com/css2?family=Cinzel:wght@400;600;700&display=swap">
<style>
  :root {
    --paper: #e4e4e4;
    --crop: #6f6f6f;
    --leather-dark: #0d0d0d;
    --leather-mid: #242424;
    --spine-shade: #080808;
    --gold: #e8b625;
    --gold-deep: #b98510;
    --gold-light: #f6d35c;
    --ink-white: #f4f4f4;
    --scene-top: #1c2536;
    --scene-bottom: #2b3346;
  }
  * { margin: 0; padding: 0; box-sizing: border-box; }
  html, body {
    width: 1200px; height: 876px; overflow: hidden;
    background: var(--paper);
  }
  .canvas { position: relative; width: 1200px; height: 876px; }

  .crop-marks { position: absolute; inset: 0; }

  .spread {
    position: absolute; left: 101px; top: 115px; width: 998px; height: 641px;
    background:
      radial-gradient(ellipse at 30% 30%, var(--leather-mid) 0%, var(--leather-dark) 75%),
      var(--leather-dark);
    box-shadow: 0 2px 6px rgba(0,0,0,0.35);
    overflow: hidden;
  }
  .spread::before {
    content: ""; position: absolute; inset: 0;
    background: radial-gradient(ellipse at 75% 40%, rgba(60,60,60,0.35) 0%, rgba(0,0,0,0) 65%);
  }
  .spine {
    position: absolute; left: 487px; top: 0; width: 12px; height: 100%;
    background: linear-gradient(90deg, rgba(0,0,0,0.2), var(--spine-shade) 50%, rgba(0,0,0,0.2));
  }

  .front-cover {
    position: absolute; left: 499px; top: 0; width: 499px; height: 100%;
    font-family: "Cinzel", serif;
    text-align: center;
  }

  .edition-badge {
    position: absolute; left: 417px; top: 29px; width: 60px; height: 60px;
    border-radius: 50%;
    background: radial-gradient(circle at 40% 35%, var(--gold-light), var(--gold) 55%, var(--gold-deep));
    color: #1a1a1a; display: flex; flex-direction: column;
    align-items: center; justify-content: center; line-height: 1;
  }
  .edition-badge .number { font-size: 17px; font-weight: 700; }
  .edition-badge .label { font-size: 8px; font-weight: 600; margin-top: 1px; }

  .title {
    position: absolute; left: 0; right: 0; top: 94px;
    color: var(--gold); font-weight: 600; line-height: 1.05;
    text-shadow: 0 1px 2px rgba(0,0,0,0.6);
  }
  .title .line-lead { display: block; font-size: 44px; }
  .title .line-sub { display: block; font-size: 36px; margin-top: 4px; }

  .subtitle {
    position: absolute; left: 0; right: 0; top: 238px;
    color: var(--ink-white); font-size: 20px; line-height: 31px; font-weight: 400;
  }

  .scene-frame {
    position: absolute; left: 51px; top: 331px; width: 406px; height: 216px;
    border: 6px solid var(--gold);
  }
  .scene-image {
    width: 100%; height: 100%;
    background: linear-gradient(180deg, var(--scene-top) 0%, var(--scene-bottom) 100%);
  }

  .author {
    position: absolute; left: 0; right: 0; top: 583px;
    display: flex; align-items: center; justify-content: center; gap: 14px;
    color: var(--gold); font-size: 20px; font-weight: 600;
  }
  .author .rule { width: 58px; height: 2px; background: var(--gold); }
</style>
</head>
<body>
<div class="canvas">
  <svg class="crop-marks" width="1200" height="876" viewBox="0 0 1200 876" aria-hidden="true">
    <g stroke="#6f6f6f" stroke-width="1.2">
      <line x1="101" y1="60" x2="101" y2="100"/><line x1="46" y1="115" x2="86" y2="115"/>
      <line x1="1099" y1="60" x2="1099" y2="100"/><line x1="1114" y1="115" x2="1154" y2="115"/>
      <line x1="101" y1="771" x2="101" y2="811"/><line x1="46" y1="756" x2="86" y2="756"/>
      <line x1="1099" y1="771" x2="1099" y2="811"/><line x1="1114" y1="756" x2="1154" y2="756"/>
      <line x1="588" y1="75" x2="588" y2="100"/><line x1="600" y1="75" x2="600" y2="100"/>
      <line x1="588" y1="771" x2="588" y2="796"/><line x1="600" y1="771" x2="600" y2="796"/>
    </g>
  </svg>

  <div class="spread">
    <div class="spine"></div>

    <section class="front-cover">
      <div class="edition-badge">
        <span class="number">3nd</span>
        <span class="label">Edition</span>
      </div>

      <h1 class="title">
        <span class="line-lead">The Bramblewood</span>
        <span class="line-sub">Roadside Defense</span>
        <span class="line-sub">Guide</span>
      </h1>

      <p class="subtitle">An Owner's Notes on Quietly<br>Settling Every Old Dispute</p>

      <div class="scene-frame">
        <div class="scene-image" role="img" aria-label="Photograph of police cars on a street at night"></div>
      </div>

      <p class="author"><span class="rule"></span>Owen T. Marsh, Esq.<span class="rule"></span></p>
    </section>
  </div>
</div>
</body>
</html>
```